Business Cards for New Club President

I would like to get Business cards for the new president of our club. Our organization used Pixel Harbor last year to create a logo for an event and we love that logo. The new president really likes the logo and would like to use it for her personal logo. But since it was created for a specific event, it needs to be modified. She would like to keep the same basic design but add a strand of pearls winding through the image.

Contact Information for Business Card

Name of President, email, phone, location

Font styles to use
Serif

Colors
ec1f27
fff4ee

Requirements
Must have
• 1. A modified version of the image we previously purchased from Pixel Harbor. (see uploaded image); remove the name of the event and date..
2. A strand of pearls (or individual pearls) gracefully wrapping through the image.
3. The phrase "Maribel Alumnae" or "Maribel Alumnae Chapter" on the design
Nice to have
• Use the original design we purchased from Pixel Harbor
Should not have
• Should not have any other colors other than red, white or black.

```html
<!DOCTYPE html>
<html lang="en">
<head>
<meta charset="utf-8">
<title>Maribel Alumnae – Business Card</title>
<link rel="stylesheet" href="https://fonts.googleapis.com/css2?family=Source+Serif+4:wght@400;700&display=swap">
<style>
  :root {
    --brand-red: #c01e2e;
    --brand-red-deep: #a3192a;
    --ink: #2e2e2e;
    --ink-soft: #555555;
    --paper: #ffffff;
    --backdrop: #ecebea;
  }
  * { box-sizing: border-box; margin: 0; padding: 0; }
  html, body { width: 1200px; height: 800px; overflow: hidden; }
  body {
    background: var(--backdrop);
    font-family: "Source Serif 4", Georgia, serif;
    display: flex;
    align-items: center;
    justify-content: center;
    gap: 60px;
  }
  .card {
    width: 490px;
    height: 280px;
    position: relative;
    box-shadow: 0 6px 18px rgba(0,0,0,0.12);
  }
  .card--front {
    background: var(--brand-red);
    display: flex;
    align-items: center;
    justify-content: center;
  }
  .brand-mark {
    display: flex;
    align-items: center;
    gap: 10px;
  }
  .brand-mark__square { width: 22px; height: 22px; flex: none; }
  .brand-mark__name {
    font-weight: 700;
    text-transform: uppercase;
    letter-spacing: 0.06em;
    white-space: nowrap;
  }
  .card--front .brand-mark__square { background: var(--brand-red-deep); }
  .card--front .brand-mark__name { color: var(--brand-red-deep); font-size: 30px; }

  .card--back { background: var(--paper); }
  .card--back .brand-mark {
    position: absolute;
    top: 40px;
    right: 34px;
  }
  .card--back .brand-mark__square { background: var(--brand-red); width: 16px; height: 16px; }
  .card--back .brand-mark__name { color: var(--brand-red); font-size: 19px; }

  .contact {
    position: absolute;
    left: 36px;
    bottom: 30px;
    color: var(--ink-soft);
    font-size: 16px;
    line-height: 1.3;
  }
  .contact__org {
    color: var(--brand-red);
    font-weight: 700;
    text-transform: uppercase;
    font-size: 17px;
  }
  .contact__name { color: var(--ink); font-weight: 700; }
  .contact__line { display: flex; align-items: center; gap: 6px; }
  .contact__icon { width: 13px; height: 13px; fill: var(--brand-red); flex: none; }
</style>
</head>
<body>
  <section class="card card--front" aria-label="Card front">
    <div class="brand-mark">
      <span class="brand-mark__square"></span>
      <span class="brand-mark__name">Maribel Alumnae</span>
    </div>
  </section>

  <section class="card card--back" aria-label="Card back">
    <div class="brand-mark">
      <span class="brand-mark__square"></span>
      <span class="brand-mark__name">Maribel Alumnae</span>
    </div>
    <div class="contact">
      <p class="contact__org">Maribel Alumnae</p>
      <p class="contact__name">Elena Marsh, President</p>
      <p>Harbor Crest Avenue, Suite</p>
      <p>210 Bayview, USA</p>
      <p class="contact__line">
        <svg class="contact__icon" viewBox="0 0 16 16" aria-hidden="true"><path d="M2 5c0-2 2-3 6-3s6 1 6 3v1h-3V5H5v1H2zM4 7h8l2 7H2z"/></svg>
        555.204.7180
      </p>
      <p class="contact__line">
        <svg class="contact__icon" viewBox="0 0 16 16" aria-hidden="true"><path d="M1 3h14v10H1zM2 4.5v.5l6 4 6-4v-.5z"/></svg>
        hello@maribelclub.org
      </p>
    </div>
  </section>
</body>
</html>
```